K7 Solutions business card design contest. Use logo and create a professional layout.

See attached sample. Please sharpen all text and images, don't want any pix-elated content. We are looking for a clean look that quickly provides the information need. Please include our information provided on the sample card. Please feel free to offer any design changes. Please only user the colors provided: #2D3539 & #FFA500. Do not prefer any images other than the K7 Logo

Target Market(s)

Construction, Architects, General Contractors, residential

Industry/Entity Type

Business

Contact Information for Business Card

Company logo, Name, email, fax & phone

Font styles to use
Other font styles liked:
• Josefin Slab

Requirements
Must have
• Name
• Phone & Fax #'s
• address
• Logo
• Website url: www.kq7solutions.example
Nice to have
• Font Colors #2D3539 & #FFA400
• We prefer a white background.

```html
<!DOCTYPE html>
<html lang="en">
<head>
<meta charset="utf-8">
<title>K7 Solutions – Business Card</title>
<link href="https://fonts.googleapis.com/css2?family=Josefin+Slab:wght@400;600;700&display=swap" rel="stylesheet">
<style>
  :root {
    --ink: #2D3539;
    --ink-soft: #4a4f52;
    --orange: #FFA500;
    --card-orange: #FBA521;
    --paper: #ffffff;
    --backdrop: #e6e6ea;
  }
  * { box-sizing: border-box; margin: 0; padding: 0; }
  html, body {
    width: 1200px; height: 686px; overflow: hidden;
    background: var(--backdrop);
    font-family: "Josefin Slab", Georgia, serif;
  }
  .stage { position: relative; width: 1200px; height: 686px; }

  .card {
    position: absolute; top: 202px;
    width: 494px; height: 281px;
  }
  .card--front {
    left: 97px; background: var(--paper);
    border: 1px solid var(--orange);
  }
  .card--back { left: 610px; background: var(--card-orange); }

  .brand { text-align: center; }
  .brand__name {
    font-weight: 700; color: var(--ink);
    font-size: 28px; line-height: 1; letter-spacing: 0.2px;
  }
  .brand__tagline {
    font-weight: 700; color: var(--ink);
    font-size: 13px; margin-top: 3px;
  }
  .brand__services {
    font-weight: 600; color: var(--ink-soft);
    font-size: 12.5px; letter-spacing: 0.8px; margin-top: 4px;
  }
  .card--front .brand { position: absolute; top: 33px; left: 0; right: 0; }

  .person { position: absolute; top: 133px; left: 0; right: 0; text-align: center; }
  .person__name {
    color: var(--orange); font-weight: 600; font-size: 21px; letter-spacing: 0.6px;
  }
  .person__title { color: var(--ink); font-size: 13px; margin-top: 5px; }

  .divider {
    position: absolute; top: 189px; left: 0; right: 0;
    height: 2px; background: var(--orange);
  }

  .contact {
    position: absolute; top: 207px; left: 0; right: 0;
    text-align: center; color: var(--ink); font-size: 11px; line-height: 23px;
  }
  .contact .sep { margin: 0 7px; }

  .card--back .brand {
    position: absolute; top: 0; bottom: 0; left: 0; right: 0;
    display: flex; flex-direction: column; justify-content: center; align-items: center;
  }
  .card--back .brand__name { color: var(--paper); font-size: 46px; }
  .card--back .brand__tagline { color: var(--paper); font-size: 21px; margin-top: 6px; }
</style>
</head>
<body>
<main class="stage">
  <section class="card card--front">
    <div class="brand">
      <div class="brand__name">K7 Solutions</div>
      <div class="brand__tagline">Every Site, Seen Clearly</div>
      <div class="brand__services">Drone | Webcam | Video</div>
    </div>
    <div class="person">
      <div class="person__name">Martin R. Hale, MBA</div>
      <div class="person__title">Director of Operations</div>
    </div>
    <div class="divider"></div>
    <div class="contact">
      <div>Office : 2140 Alder Ridge Road, Suite 210-118 Brookfield, Georgia, 30999</div>
      <div>Phone : (555) 014 - 2210<span class="sep">/</span>Fax : (555) 014 - 7735<span class="sep">/</span>E-mail : info@kq7solutions.example</div>
      <div>Web : www.kq7solutions.example</div>
    </div>
  </section>

  <section class="card card--back">
    <div class="brand">
      <div class="brand__name">K7 Solutions</div>
      <div class="brand__tagline">Every Site, Seen Clearly</div>
    </div>
  </section>
</main>
</body>
</html>
```